coaching agenda

Please redesign the brochure attached in a more modern/trendy out look. I want something completely different to what is attached but using the same colours and logo.

```html
<!DOCTYPE html>
<html lang="en">
<head>
<meta charset="utf-8">
<title>Coaching Session Brochure</title>
<link href="https://fonts.googleapis.com/css2?family=Baumans&family=Open+Sans:wght@400;600;700&family=Russo+One&display=swap" rel="stylesheet">
<style>
:root{
  --blue:#1aa3e8;
  --blue-deep:#0b82cc;
  --blue-soft:#4cb9f0;
  --blue-year:#8fd3f7;
  --yellow:#ffd91c;
  --ink:#333a40;
  --muted:#555d63;
  --num:#9aa6ad;
  --grey-top:#c9cbcd;
  --grey-bottom:#eceded;
  --stage:#e6e7e9;
  --white:#ffffff;
}
*{margin:0;padding:0;box-sizing:border-box}
html,body{width:1200px;height:1200px;overflow:hidden;background:var(--stage)}
body{position:relative;font-family:"Open Sans",sans-serif;color:var(--ink)}
.page{position:absolute;background:var(--white);overflow:hidden}
.abs{position:absolute}
.display{font-family:"Baumans",sans-serif;font-weight:400}

.brand{font-weight:600;color:var(--ink);display:flex;align-items:center;gap:6px}
.brand .dot{width:10px;height:10px;border-radius:50%;background:var(--blue)}

/* back page */
.back{left:167px;top:70px;width:405px;height:522px}
.back-head{left:0;top:0;width:405px;height:110px;background:linear-gradient(180deg,var(--grey-top),var(--grey-bottom))}
.back-title{left:34px;top:72px;font-size:20px;color:var(--ink)}
.back-copy{left:34px;top:140px;width:340px;font-size:7.4px;line-height:1.5}
.back-copy p{margin-bottom:10px}
.bullets{left:34px;top:234px;font-size:5.8px;line-height:1.45;list-style:none}
.bullets li::before{content:"• ";color:var(--blue)}
.back-brand{left:41px;top:370px;font-size:13px}
.back-foot{left:0;top:429px;width:405px;height:93px;background:var(--blue)}
.contact{left:42px;top:26px;list-style:none;color:var(--white);font-size:8px;font-style:italic;line-height:1.9}
.contact li{display:flex;align-items:center;gap:8px}
.phone-pill{left:274px;top:38px;width:100px;height:21px;border-radius:6px;background:var(--blue-deep);border:1px solid var(--blue-soft);color:var(--white);font-size:10px;display:flex;align-items:center;justify-content:center}

/* cover */
.cover{left:650px;top:70px;width:405px;height:522px;background:var(--blue)}
.cover-top{left:0;top:0;width:405px;height:111px;background:var(--white)}
.cover-brand{left:56px;top:40px;font-size:14px}
.cover-sub{left:56px;top:62px;font-size:5px;color:var(--muted)}
.note{left:49px;top:111px;width:120px;height:119px;background:var(--yellow);clip-path:polygon(0 0,100% 0,100% 78%,78% 100%,0 100%)}
.note-text{left:25px;top:32px;font-family:"Russo One",sans-serif;font-size:14px;line-height:1.1;color:var(--ink)}
.portrait{left:222px;top:38px;width:120px;height:460px;border-radius:50px 50px 6px 6px;background:linear-gradient(180deg,#c9ccd3 0%,#2a3140 30%,#1d2330 100%)}
.cover-web{left:63px;top:476px;font-size:8px;color:var(--white)}

/* spread */
.spread{left:198px;top:633px;width:796px;height:514px}
.spread-head{left:0;top:0;width:796px;height:109px;background:linear-gradient(90deg,var(--blue) 0%,var(--blue) 50%,var(--blue-soft) 50%,var(--blue) 100%)}
.spread-title{top:72px;font-size:19px;line-height:24px;color:var(--white)}
.spread-title .year{color:var(--blue-year);font-family:"Open Sans",sans-serif;font-weight:700;font-size:21px}
.fold{left:397px;top:0;width:3px;height:514px;background:linear-gradient(90deg,rgba(0,0,0,.07),rgba(0,0,0,0))}

.questions{left:44px;top:128px;list-style:none;font-size:7.4px;line-height:1;color:var(--ink)}
.questions li{margin-bottom:9.6px}
.gets{left:44px;top:232px;font-size:12px;color:var(--blue);line-height:1.2}
.gets span{display:block;color:var(--ink);font-size:11px}

.numlist{list-style:none;color:var(--ink)}
.numlist li{display:flex;gap:4px}
.numlist b{font-weight:400;color:var(--num);min-width:10px;text-align:right;flex:none}
.numlist small{display:block;font-size:5px;line-height:1.4}

.col-a,.col-b{top:278px;font-size:6.2px;line-height:1.3}
.col-a{left:44px;width:172px}
.col-b{left:222px;width:165px}
.col-a li,.col-b li{margin-bottom:7.5px}
.col-a b,.col-b b{font-size:8.5px;line-height:1}
.left-web{left:280px;top:476px;width:90px;text-align:right;font-size:7.5px;color:var(--blue)}
.left-rule{left:44px;top:486px;width:326px;height:1px;background:#e3e5e7}

.lead{left:433px;top:128px;width:330px;font-size:7px;font-weight:700;color:var(--blue);line-height:1.3}
.lead p{margin-bottom:8px}

.col-c{left:432px;top:206px;width:142px;font-size:5.5px;line-height:1.3}
.col-c li{margin-bottom:9px;font-weight:700}
.col-c b{font-size:8px;line-height:1}
.sub-grid{display:grid;grid-template-columns:1fr 1fr;gap:0 4px;font-weight:400;font-size:4.8px;line-height:1.35;margin-top:3px}
.sub-grid span::before{content:"• ";color:var(--blue)}

.col-d{left:610px;top:206px;width:155px;font-size:5.5px}
.col-d h4{font-weight:700;font-size:5.6px;display:flex;gap:4px;align-items:baseline}
.col-d h4 b{font-weight:400;color:var(--num);font-size:8px}
.para{font-size:4.8px;line-height:1.42;text-align:justify;margin:3px 0 5px}
.four{display:grid;grid-template-columns:repeat(4,1fr);font-size:4.8px;line-height:1.45;margin-bottom:8px}
.four span::before{content:"• ";color:var(--blue)}
.tips{list-style:none;font-size:4.8px;line-height:1.42;margin-top:3px;padding-left:6px}
.tips li::before{content:"• ";color:var(--blue)}
.years{left:610px;top:464px;width:155px;display:grid;grid-template-columns:repeat(4,1fr);text-align:center;font-size:8px;font-weight:700;color:var(--blue);line-height:1.1}
.years small{display:block;font-size:5px;font-weight:400;color:var(--ink)}
</style>
</head>
<body>

<section class="page back">
  <div class="abs back-head"></div>
  <h2 class="abs back-title display">What are your behaviours costing you</h2>
  <div class="abs back-copy">
    <p>Public domain – those areas where people see you acting on your behaviours, both positive &amp; negative. Professionalism, application, integrity, self-esteem, respect for others &amp; proficiency are on display here</p>
    <p>Private domain – is the one where we spend time with ourselves &amp; where our mind games play out. This is the biggest behavioural game of all as we confront our habits, limitations, acceptance of disruptions, temptations &amp; fears</p>
  </div>
  <ul class="abs bullets">
    <li>Know your CRM system</li>
    <li>Capture data &amp; use it to generate an income</li>
    <li>Buyer work</li>
    <li>6 weeks after settlement</li>
    <li>Significantly increase the number of “just listed” you drop</li>
    <li>Put a name to a property</li>
  </ul>
  <div class="abs brand back-brand"><span class="dot"></span>Morgan Hale</div>
  <div class="abs back-foot">
    <ul class="abs contact">
      <li><svg width="9" height="10" viewBox="0 0 10 12"><path d="M5 0a4 4 0 0 0-4 4c0 3 4 8 4 8s4-5 4-8a4 4 0 0 0-4-4zm0 5.6A1.6 1.6 0 1 1 5 2.4a1.6 1.6 0 0 1 0 3.2z" fill="#fff"/></svg>PO Box 4200, Riverside WA 6000</li>
      <li><svg width="9" height="8" viewBox="0 0 10 8"><rect x=".5" y=".5" width="9" height="7" fill="none" stroke="#fff"/><path d="M.5 .5 5 4.5 9.5 .5" fill="none" stroke="#fff"/></svg>morgan@halecoaching.example</li>
      <li><svg width="9" height="9" viewBox="0 0 10 10"><circle cx="5" cy="5" r="4.4" fill="none" stroke="#fff"/><path d="M.6 5h8.8M5 .6c-2.4 2.6-2.4 6.2 0 8.8M5 .6c2.4 2.6 2.4 6.2 0 8.8" fill="none" stroke="#fff" stroke-width=".8"/></svg>www.halecoaching.example</li>
    </ul>
    <div class="abs phone-pill">+61 400 000 123</div>
  </div>
</section>

<section class="page cover">
  <div class="abs cover-top"></div>
  <div class="abs brand cover-brand"><span class="dot"></span>Morgan Hale</div>
  <div class="abs cover-sub">Hale Sales Coaching Pty Ltd</div>
  <div class="abs note"><div class="abs note-text">COACHING<br>SESSION<br>JUNE<br>2018</div></div>
  <div class="abs portrait" role="img" aria-label="Full-length portrait of the coach in a dark suit"></div>
  <div class="abs cover-web">www.halecoaching.example</div>
</section>

<section class="page spread">
  <div class="abs spread-head"></div>
  <h2 class="abs spread-title display" style="left:44px">Yesterday – Today – Tomorrow</h2>
  <h2 class="abs spread-title display" style="left:433px">Today onwards <span class="year">2018</span></h2>

  <ul class="abs questions">
    <li>How many appraisals/listing presentations are booked in your diary for this week?</li>
    <li>How many appraisals/listing presentations are booked in your diary for next week?</li>
    <li>How many second viewings/private viewings are booked in your diary for this week?</li>
    <li>How many listings will you launch this week?</li>
  </ul>
  <div class="abs gets display">2018 / 2019 Productivity Gets<span>There's more to it than numbers:</span></div>

  <ol class="abs numlist col-a">
    <li><b>1.</b><span>Increase in market share in your core area</span></li>
    <li><b>2.</b><span>Increase in commission rates</span></li>
    <li><b>3.</b><span>Relationships [ data base growth]-<br>future sellers</span></li>
    <li><b>4.</b><span>Relationships [ data base growth]-<br>buyer prospects</span></li>
    <li><b>5.</b><span>Number of appointments / appraisals booked<br>each week</span></li>
    <li><b>6.</b><span>Listing pipeline growth</span></li>
    <li><b>7.</b><span>Skills development –is an opportunity -<small>you can't be defined as not knowing what to do. Be specific. You can't become a better closer if you don't have people to close on!!</small></span></li>
    <li><b>8.</b><span>Managing free time –<br>you can't be defined by time</span></li>
  </ol>
  <ol class="abs numlist col-b">
    <li><b>9.</b><span>Time is an opportunity</span></li>
    <li><b>10.</b><span>Know your data base system –<br>data base is an opportunity</span></li>
    <li><b>11.</b><span>Service charter –<br>there is opportunity in service – repeat / referrals / the future seller calls “you in”</span></li>
    <li><b>12.</b><span>Health &amp; energy leads to better recovery</span></li>
    <li><b>13.</b><span>Family &amp; self- breaks</span></li>
    <li><b>14.</b><span>Self-time</span></li>
    <li><b>15.</b><span>Milestones / benchmarks</span></li>
    <li><b>16.</b><span>Wealth creation</span></li>
  </ol>
  <div class="abs left-rule"></div>
  <div class="abs left-web">www.halecoaching.example</div>

  <div class="abs fold"></div>

  <div class="abs lead">
    <p>Build the listing pipeline so you have stock coming to market when the sun shines again</p>
    <p>Don't wait until the usual “spring selling session” promo's start to start looking for listings.</p>
    <p>Get the jump on your competition by having your July to December profile building campaign set in place now &amp; make sure it is fully funded so you don't lose profile momentum.</p>
  </div>

  <ol class="abs numlist col-c">
    <li><b>1.</b><span>What went well this month?</span></li>
    <li><b>2.</b><span>Did you convert good days into good weeks, good weeks into a good month?</span></li>
    <li><b>3.</b><span>How organised were you last week?</span></li>
    <li><b>4.</b><span>What ideas, actions, processes, systems and motivations have you introduced into your business during the last thirty days?</span></li>
    <li><b>5.</b><span>What systems do you need to implement to create a smoother work flow?</span></li>
    <li><b>6.</b><span>Are you pursuing what you believe in?</span></li>
    <li><b>7.</b><span>At what time of the day are you running at your true potential?</span></li>
    <li><b>8.</b><span>What have been your numbers for May?
      <span class="sub-grid">
        <span>Speak to's</span><span>Home opens</span>
        <span>Appointments</span><span>Negotiations</span>
        <span>Appraisals</span><span>Sales</span>
        <span>Listing presentations</span><span>Lessons learned list</span>
        <span>Listing pipeline</span><span>Inroads into the market share</span>
        <span>Listing authorities signed</span><span>In your core area - are you</span>
        <span>Listings launched</span><span>being called in?</span>
      </span></span></li>
    <li><b>9.</b><span>Script session – what was the best script you used last week?</span></li>
    <li><b>10.</b><span>Stock review</span></li>
  </ol>

  <div class="abs col-d">
    <h4><b>11.</b>Build an audience</h4>
    <p class="para">All real estate sales people have customers. Lucky ones have fans. But the most fortunate real estate sales people have audiences. An audience can be your point of difference.</p>
    <p class="para">A lot of real estate people still spend big bucks to reach people. Every time they want to say something, they dip into their marketing budgets, pull out some cash and do some “marketing”. This approach is both expensive and unreliable. As has been said, you waste half of your marketing budget, you just don't know which half.</p>
    <p class="para">Today's smart real estate sales person knows better. Instead of going out to reach people, you want people to come to you. An audience returns often – on its own – to see what you have to say. This is the most receptive group of prospective customers and customers you'll ever have.</p>
    <div class="four">
      <span>Send</span><span>Capture</span><span>Convert</span><span>Sell</span>
      <span>Say</span><span>Connect</span><span>List</span><span>Retain</span>
      <span>Connect</span><span>Present</span><span>Market</span><i></i>
    </div>
    <h4><b>12.</b>Make the uncommon common</h4>
    <ul class="tips">
      <li>Time – no time is no excuse – you cannot be defined by time in 2018/ the need to do more for less following the industry discounting of fees.</li>
      <li>How you manage free time</li>
      <li>You cannot be defined by not knowing what to do</li>
      <li>Embrace where your market is at:</li>
    </ul>
  </div>
  <div class="abs years">
    <span>2015<small>Wow</small></span><span>2016<small>Hope</small></span><span>2017<small>New norm</small></span><span>2018<small>The norm</small></span>
  </div>
</section>

</body>
</html>
```